Organic Herbs & Spices container

Greek startup company, which cultivate and trade spices and herbs (such as oregano, mint, thyme, sage etc.)

At present we are interested in only the type and shape of packaging which should be made by materials such as paper, cardboard, laminated paper and others based on paper or plastic.

Package size vary from 80g (2.82oz) - 300g (10.58oz). We are going to use the same packing for a variety of products with different information

* Please find attached our logo which should be included in the design.
* There is no company name available at the moment, however a name placeholder should be included.
* include a placeholder for the type of product (sage, oregano, mint, tea etc...).
* Each package should have a place in order to include product details and nutrition facts.

e.g.
xxxx (company name placeholder)
Sage (product type)
product details and nutrition facts.
Updates

Dear designers,first of all, thank you for your proposals. Please find bellow some updates for the project.- It is mandatory to include the logo into the design - Each package should be able to stored vertically - We are looking for one specific package design, please do not submit many variations of a certain package neither colour differentiations Thanks and good luck Added Wednesday, September 28, 2016

Please avoid the use of images. The same package will be used for all the kinds of products (only name and maybe colour will be different among different products. A transparent frame that will show the contents could be used too) Added Wednesday, September 28, 2016

Please find attached logo in EPS format

Our logo is the baseline, any concepts should be based on it. Try to avoid just adding the logo as a small sticker somewhere on the design. Please try to create around it at any way toy like. This could be, to visualize it as a 3D shape or object which can be used as the container of the products.

Reason: We would like to extend the time of the project. We believe that most of the submitted designs do not comply with our requirements.

Reason: We would like to see a bigger variety of ideas

Target Market(s)

Pretty much to anyone over 20 years old worldwide.

Industry/Entity Type

Nutrition

Requirements
Must have
• It should be attractive, easily recognized, simple yet innovative, durable, functional (easy to use) and easy to store.
Should not have
• Project must not include complex or obnoxious shapes and colours.

```html
<!DOCTYPE html>
<html lang="en">
<head>
<meta charset="utf-8">
<title>Verdalia Herb &amp; Spice Packs</title>
<link rel="stylesheet" href="https://fonts.googleapis.com/css2?family=Cinzel:wght@600&display=swap">
<style>
  :root {
    --backdrop: #f1f1f1;
    --kraft: #c8a477;
    --kraft-edge: #b38e60;
    --rim: #b9a468;
    --label-text: #f6efe0;
    --brand-text: #fff6dc;
    --oregano-band: #55661c;
    --oregano-fill: #6a6939;
    --turmeric-band: #d6860f;
    --turmeric-fill: #e0a32a;
    --paprika-band: #761a12;
    --paprika-fill: #8b2b1f;
  }
  html, body {
    margin: 0;
    padding: 0;
    overflow: hidden;
  }
  .canvas {
    position: relative;
    width: 1200px;
    height: 1000px;
    background: var(--backdrop);
    overflow: hidden;
  }
  .pack {
    position: absolute;
    width: 220px;
    height: 440px;
  }
  .pack--oregano { left: 268px; top: 220px; }
  .pack--turmeric { left: 492px; top: 335px; width: 230px; height: 460px; }
  .pack--paprika { left: 744px; top: 220px; }
  .pack svg {
    display: block;
    width: 100%;
    height: 100%;
  }
  .pack-body { fill: var(--kraft); stroke: var(--kraft-edge); stroke-width: 1.5; }
  .window-rim { fill: none; stroke: var(--rim); stroke-width: 10; }
  .product-name {
    font-family: "Cinzel", "Times New Roman", serif;
    font-weight: 600;
    font-size: 22px;
    fill: var(--label-text);
    letter-spacing: 0.5px;
  }
  .brand-name {
    font-family: "Cinzel", "Times New Roman", serif;
    font-weight: 600;
    font-size: 20px;
    fill: var(--brand-text);
  }
  .pack--oregano .band { fill: var(--oregano-band); }
  .pack--oregano .contents { fill: var(--oregano-fill); }
  .pack--turmeric .band { fill: var(--turmeric-band); }
  .pack--turmeric .contents { fill: var(--turmeric-fill); }
  .pack--paprika .band { fill: var(--paprika-band); }
  .pack--paprika .contents { fill: var(--paprika-fill); }
</style>
</head>
<body>
<main class="canvas">

  <div class="pack pack--oregano">
    <svg viewBox="0 0 220 440" aria-label="Oregano pack front">
      <rect class="pack-body" x="0" y="0" width="220" height="440"/>
      <path class="band" d="M0 0H220V82Q110 122 0 82Z"/>
      <text class="product-name" x="110" y="62" text-anchor="middle">OREGANO</text>
      <path class="contents" role="img" aria-label="Window showing dried oregano leaves"
            d="M110 122C150 152 205 200 205 292A95 95 0 0 1 15 292C15 200 70 152 110 122Z"/>
      <path class="window-rim" d="M110 122C150 152 205 200 205 292A95 95 0 0 1 15 292C15 200 70 152 110 122Z"/>
      <text class="brand-name" x="110" y="292" text-anchor="middle">Verdalia</text>
    </svg>
  </div>

  <div class="pack pack--turmeric">
    <svg viewBox="0 0 220 440" aria-label="Turmeric pack front">
      <rect class="pack-body" x="0" y="0" width="220" height="440"/>
      <path class="band" d="M0 0H220V82Q110 122 0 82Z"/>
      <text class="product-name" x="110" y="62" text-anchor="middle">TUMERIC</text>
      <path class="contents" role="img" aria-label="Window showing ground turmeric powder"
            d="M110 122C150 152 205 200 205 292A95 95 0 0 1 15 292C15 200 70 152 110 122Z"/>
      <path class="window-rim" d="M110 122C150 152 205 200 205 292A95 95 0 0 1 15 292C15 200 70 152 110 122Z"/>
      <text class="brand-name" x="110" y="292" text-anchor="middle">Verdalia</text>
    </svg>
  </div>

  <div class="pack pack--paprika">
    <svg viewBox="0 0 220 440" aria-label="Paprika pack front">
      <rect class="pack-body" x="0" y="0" width="220" height="440"/>
      <path class="band" d="M0 0H220V82Q110 122 0 82Z"/>
      <text class="product-name" x="110" y="62" text-anchor="middle">PAPRIKA</text>
      <path class="contents" role="img" aria-label="Window showing ground red paprika"
            d="M110 122C150 152 205 200 205 292A95 95 0 0 1 15 292C15 200 70 152 110 122Z"/>
      <path class="window-rim" d="M110 122C150 152 205 200 205 292A95 95 0 0 1 15 292C15 200 70 152 110 122Z"/>
      <text class="brand-name" x="110" y="292" text-anchor="middle">Verdalia</text>
    </svg>
  </div>

</main>
</body>
</html>
```